High-end construction company needs a business card design

We need a modern looking business card that draws people in, is memorable and looks so good people will want to sick it on their fridges.
On the first side what is needed are:
Logo
My name - Tomas Verbelk
Title - Managing Director
Website - www.kravel.co.uk
Email - tomas@kravel.co.uk
Telephone - 020 5194 6381
Mobile - 07845319027
On the back side was is needed is a list of all the services we provide:
-Kitchen Renovations
-Bathroom Renovations
-House Renovations
-Garage Conversions
-Extensions
-Loft Conversions
-Conservatories
-Carpentry
-Tiling
-Electrical
-Plumbing & Heating
-Bricklaying
-Landscaping
-Decorating
-Plastering
We would like the colours to be the same shades as on the logo with grey or black for the words.
Target Market(s)
Anyone who needs building work done
Contact Information for Business Card
This business card is for a construction company which strives to deliver excellent service and quality.
The look and feel of the card should represent this.
Requirements
Must have
- On the first side what is needed are:
Logo
My name - Tomas Verbelk
Title - Managing Director
Website - www.kravel.co.uk
Email - tomas@kravel.co.uk
Telephone - 020 5194 6381
Mobile - 07845319027
Nice to have
- Cool looking features

```html
<!DOCTYPE html>
<html lang="en">
<head>
<meta charset="utf-8">
<title>Kravel Construction – House-shaped Business Card Options</title>
<link rel="stylesheet" href="https://fonts.googleapis.com/css2?family=Lato:wght@400;700;900&display=swap">
<style>
  :root {
    --green-deep: #4a8c3f;
    --green-fresh: #76bc43;
    --white: #ffffff;
    --ink: #000000;
  }
  html, body {
    margin: 0;
    padding: 0;
    width: 952px;
    height: 1200px;
    overflow: hidden;
    background: var(--white);
  }
  .sheet {
    display: block;
    width: 952px;
    height: 1190px;
    font-family: "Lato", sans-serif;
  }
  .option-title { font-weight: 900; font-size: 36px; fill: var(--ink); }
  .house-deep { fill: var(--green-deep); }
  .house-fresh { fill: var(--green-fresh); }
  .house-plain { fill: var(--white); }
  .house-inline { fill: none; stroke: var(--white); stroke-width: 4; }
  .brand-name { font-weight: 900; font-size: 80px; fill: var(--white); }
  .brand-sub { font-weight: 900; font-size: 20px; fill: var(--white); }
  .person-name { font-weight: 700; font-size: 31px; fill: var(--white); }
  .person-title { font-weight: 700; font-size: 22px; fill: var(--white); }
  .contact { font-weight: 400; font-size: 18px; fill: var(--white); }
  .contact .label { font-weight: 700; }
  .services-heading { font-weight: 900; font-size: 28px; }
  .services-list { font-weight: 400; font-size: 18px; }
</style>
</head>
<body>
<svg class="sheet" viewBox="0 0 1200 1500" xmlns="http://www.w3.org/2000/svg">
  <defs>
    <filter id="soft-shadow" x="-10%" y="-10%" width="120%" height="120%">
      <feDropShadow dx="0" dy="1" stdDeviation="3" flood-color="#000" flood-opacity="0.12"/>
    </filter>
    <g id="front-content">
      <text class="brand-name" x="202" y="362" textLength="298" lengthAdjust="spacingAndGlyphs">KRAVEL</text>
      <text class="brand-sub" x="202" y="387" textLength="298" lengthAdjust="spacing">CONSTRUCTION LTD</text>
      <text class="person-name" x="351" y="480" text-anchor="middle">Tomas Verbelk</text>
      <text class="person-title" x="351" y="508" text-anchor="middle">Managing Director</text>
      <text class="contact" x="351" y="556" text-anchor="middle"><tspan class="label">Website</tspan>: www.kravel.co.uk</text>
      <text class="contact" x="351" y="578" text-anchor="middle"><tspan class="label">Email</tspan>: tomas@kravel.co.uk</text>
      <text class="contact" x="351" y="601" text-anchor="middle"><tspan class="label">Telephone</tspan>: 020 5194 6381</text>
      <text class="contact" x="351" y="623" text-anchor="middle"><tspan class="label">Mobile</tspan>: 07845319027</text>
    </g>
    <g id="services-content">
      <text class="services-heading" x="850" y="288" text-anchor="middle">OUR SERVICES</text>
      <g class="services-list" text-anchor="middle">
        <text x="850" y="321">Kitchen Renovations</text>
        <text x="850" y="343">Bathroom Renovations</text>
        <text x="850" y="366">House Renovations</text>
        <text x="850" y="388">Garage Conversions</text>
        <text x="850" y="410">Extensions</text>
        <text x="850" y="433">Loft Conversions</text>
        <text x="850" y="455">Conservatories</text>
        <text x="850" y="477">Carpentry</text>
        <text x="850" y="500">Tiling</text>
        <text x="850" y="522">Electrical</text>
        <text x="850" y="544">Plumbing &amp; Heating</text>
        <text x="850" y="567">Bricklaying</text>
        <text x="850" y="589">Landscaping</text>
        <text x="850" y="611">Decorating</text>
        <text x="850" y="634">Plastering</text>
      </g>
    </g>
  </defs>

  <g class="option option-one">
    <text class="option-title" x="600" y="106" text-anchor="middle">Option 1</text>
    <path class="house-deep" d="M351,77 L102,351 L145,351 L145,700 L558,700 L558,351 L600,351 Z"/>
    <path class="house-inline" d="M351,97 L128,345 L157,345 L157,688 L546,688 L546,345 L574,345 Z"/>
    <use href="#front-content"/>
    <path class="house-plain" filter="url(#soft-shadow)" d="M850,77 L602,351 L643,351 L643,700 L1058,700 L1058,351 L1100,351 Z"/>
    <use href="#services-content" fill="#4a8c3f"/>
  </g>

  <g class="option option-two" transform="translate(0,734)">
    <text class="option-title" x="600" y="106" text-anchor="middle">Option 2</text>
    <path class="house-fresh" d="M351,77 L102,351 L145,351 L145,700 L558,700 L558,351 L600,351 Z"/>
    <path class="house-inline" d="M351,97 L128,345 L157,345 L157,688 L546,688 L546,345 L574,345 Z"/>
    <use href="#front-content"/>
    <path class="house-fresh" d="M850,77 L602,351 L643,351 L643,700 L1058,700 L1058,351 L1100,351 Z"/>
    <use href="#services-content" fill="#ffffff"/>
  </g>
</svg>
</body>
</html>
```